Business Card Design

I am an Event and Wedding Planner in need of an eye catching business card featuring my logo (attached), my contact details, and my company tagline (Making each one of your gatherings radiant...) I would like the tagline in font similar the logo's font.
Updates
I have just noticed that my logo has a misspelling so for the final design, I will be uploading a corrected logo as soon as I have it.
My apologies.
Reason: Waiting on a corrected logo...Occasions is misspelled and it should say Weddings not Wedding
The logo has been corrected so now Occasions is spelled correctly and it says Weddings instead of Wedding. Please use Edwardian Script ITC as the font for the tagline so it will match the logo. Thank you for your patience.
Target Market(s)
Engaged couples and people hosting milestone celebrations. 25-50 years old, predominately female
Industry/Entity Type
Business
Contact Information for Business Card
Delphine Marsh, Event Manager / Owner, Mobile: 0491 836 254, Email: delphine@radiantgatheringsco.com.au, www.radiantgatheringsco.com.au, Making each one of your gatherings radiant...

```html
<!DOCTYPE html>
<html lang="en">
<head>
<meta charset="utf-8">
<title>Delphine Marsh – Business Card</title>
<link rel="stylesheet" href="https://fonts.googleapis.com/css2?family=Great+Vibes&family=Parisienne&display=swap">
<style>
  :root {
    --card-base: #fbf3f8;
    --card-tint: #f1dcea;
    --name-violet: #9a2fe3;
    --ink: #111111;
    --tagline-red: #e3211d;
  }
  * { margin: 0; padding: 0; box-sizing: border-box; }
  html, body {
    width: 1200px;
    height: 742px;
    overflow: hidden;
    background: var(--card-base);
  }
  .card {
    position: relative;
    width: 1200px;
    height: 742px;
    overflow: hidden;
  }
  .card__damask {
    position: absolute;
    inset: 0;
    background: radial-gradient(ellipse at 50% 45%, #fefbfd 0%, var(--card-base) 45%, var(--card-tint) 100%);
  }
  .card__line {
    position: absolute;
    left: 0;
    width: 100%;
    text-align: center;
    line-height: 1;
    white-space: nowrap;
    font-family: "Parisienne", cursive;
    color: var(--ink);
  }
  .card__name {
    top: 160px;
    font-family: "Great Vibes", cursive;
    font-size: 60px;
    color: var(--name-violet);
  }
  .card__role { top: 257px; font-size: 23px; }
  .card__mobile { top: 306px; font-size: 32px; }
  .card__email { top: 361px; font-size: 32px; }
  .card__web { top: 417px; font-size: 30px; }
  .card__tagline {
    top: 478px;
    font-family: "Great Vibes", cursive;
    font-size: 54px;
    color: var(--tagline-red);
  }
</style>
</head>
<body>
  <main class="card">
    <div class="card__damask" role="img" aria-label="Soft pale pink damask pattern background"></div>
    <p class="card__line card__name">Delphine Marsh</p>
    <p class="card__line card__role">Event Manager | Owner</p>
    <p class="card__line card__mobile">Mobile: 0491 836 254</p>
    <p class="card__line card__email">Email: delphine@radiantgatheringsco.com.au</p>
    <p class="card__line card__web">www.radiantgatheringsco.com.au</p>
    <p class="card__line card__tagline">Making each one of your gatherings radiant...</p>
  </main>
</body>
</html>
```